Clean Modern Skin Product branding/ label.

I need a label for a skincare line. The company is Velunda but product names will vary. A couple products to list are:
Sensitive Cleanser, Clarel, Tovane, Olva up, Halden, Halden Plus, Halden Intense, Tamby, Morwen and Quillet.

I would like the color scheme to be muted greens, grays, tourquise. The bottles are white, boston shaped with pumps, and ounces are 2, 4, 8, 16 ounces. When I choose the design, I can give you exact label sizes. Along with the ingredience already on the product label.

The look I desire is clean, minimal. A modern, organic look. Ideas that come to mind are a Voravel,https://www.voravel-example.com/product/2841/66302/4-step/step-3-polish/glowing-tonic-2 and the simplicity of Osta Vi.

Both styles high light the name, in this case Velunda, and then the specific product.

My product is clean utilizing pure ingredients rather that a bunch fillers and binders. When I work with my clients I normally will say we need to "restore the balance" from over use of harsh products. That is why this lines works. It restores the skin to it's natural state. The process is simple, so I would like the label to reflect that simplicity.

Target Market(s)

Anyone with sensitive skin. So gender neutral

Industry/Entity Type

Skin Care Product

Font styles to use
Serif
Sans Serif
Decorative

Colors
acd037
33b8a4
fcfefd
85cae6
d3d3d3

Requirements
Must have
• Logo, name of product and color identity for cleanser, Active products, moisturizers
• I am thinking we could have one color for a cleanser and a space where I can put a sticker on which cleanser it is. Acne Cleasner, Sensitive Cleanser, and Cleanser.
Nice to have
• Not sure....suprise me. I would like the font to stay the same on the VELUNDA, but you can change color, or color of leaf.
Should not have
• Too busy, too crowded or look like every other skincare line

```html
<!DOCTYPE html>
<html lang="en">
<head>
<meta charset="utf-8">
<title>Velunda Sensitive Cleanser – Label Samples</title>
<link rel="stylesheet" href="https://fonts.googleapis.com/css2?family=Oswald:wght@300;500&family=Questrial&display=swap">
<style>
  :root {
    --canvas: #ebebeb;
    --sample-grey: #a9a9a9;
    --label-white: #fcfefd;
    --label-mist: #eef0ef;
    --teal: #25a592;
    --teal-deep: #3dbcaa;
    --teal-light: #86d6c9;
    --charcoal: #2e2c2b;
    --forest: #163a34;
    --ink: #1d1d1d;
    --white: #ffffff;
  }
  * { box-sizing: border-box; margin: 0; padding: 0; }
  html, body { width: 1200px; height: 1200px; overflow: hidden; }
  body { background: var(--canvas); font-family: "Questrial", sans-serif; position: relative; }

  .label {
    position: absolute;
    top: 452px;
    width: 346px;
    height: 624px;
    overflow: hidden;
  }
  .label--white { left: 178px; }
  .label--teal { left: 704px; }

  .label__ground { position: absolute; inset: 0; }
  .label--white .label__ground {
    background: linear-gradient(135deg, var(--label-mist) 0%, var(--label-white) 45%, var(--label-white) 100%);
  }
  .label--teal .label__ground {
    background: linear-gradient(100deg, var(--teal-light) 0%, var(--teal-deep) 40%, var(--teal) 70%, var(--teal-deep) 100%);
  }

  .vertical {
    position: absolute;
    white-space: nowrap;
    line-height: 1;
    transform-origin: left bottom;
    transform: rotate(-90deg) translateY(100%);
  }

  .brand {
    left: 58px;
    bottom: 30px;
    font-family: "Questrial", sans-serif;
    font-size: 118px;
    letter-spacing: -4px;
  }
  .label--white .brand { color: var(--charcoal); }
  .label--teal .brand { color: var(--white); }

  .product-type {
    left: 170px;
    bottom: 254px;
    font-family: "Oswald", sans-serif;
    font-weight: 300;
    font-size: 64px;
    letter-spacing: -1px;
  }
  .product-name {
    left: 228px;
    bottom: 256px;
    font-family: "Oswald", sans-serif;
    font-weight: 500;
    font-size: 84px;
    letter-spacing: 1px;
  }
  .label--white .product-type,
  .label--white .product-name { color: var(--teal); }
  .label--teal .product-type { color: var(--forest); }
  .label--teal .product-name { color: var(--white); }

  .benefit {
    position: absolute;
    left: 170px;
    top: 422px;
    width: 170px;
  }
  .benefit__lead { font-size: 16px; letter-spacing: 0.2px; line-height: 1; }
  .benefit__title { font-size: 25px; line-height: 1.05; }
  .benefit__copy { font-size: 10.5px; line-height: 1.4; margin-top: 4px; color: var(--ink); }
  .label--white .benefit__lead,
  .label--white .benefit__title { color: var(--teal); }
  .label--teal .benefit__lead,
  .label--teal .benefit__title { color: var(--white); }

  .net-weight {
    position: absolute;
    left: 168px;
    top: 566px;
    font-size: 15px;
    line-height: 1.2;
  }
  .label--white .net-weight { color: var(--teal); }
  .label--teal .net-weight { color: var(--white); }

  .sample-tag {
    bottom: 236px;
    font-family: "Questrial", sans-serif;
    font-size: 32px;
    letter-spacing: 2px;
    color: var(--sample-grey);
  }
  .sample-tag--one { left: 566px; }
  .sample-tag--two { left: 1068px; }
</style>
</head>
<body>

  <section class="label label--white">
    <div class="label__ground" role="img" aria-label="Soft white label ground with a faint diamond pattern"></div>
    <div class="vertical brand">Velunda</div>
    <div class="vertical product-type">SENSITIVE</div>
    <div class="vertical product-name">CLEANSER</div>
    <div class="benefit">
      <p class="benefit__lead">PREPS SKIN FOR</p>
      <p class="benefit__title">MOISTURIZER</p>
      <p class="benefit__copy">exfoliated skin is more receptive to hydration and treatment products.</p>
    </div>
    <p class="net-weight">Net Weight<br>Goes Here</p>
  </section>
  <div class="vertical sample-tag sample-tag--one">SAMPLE 1</div>

  <section class="label label--teal">
    <div class="label__ground" role="img" aria-label="Turquoise gradient label ground with a faint large leaf motif"></div>
    <div class="vertical brand">Velunda</div>
    <div class="vertical product-type">SENSITIVE</div>
    <div class="vertical product-name">CLEANSER</div>
    <div class="benefit">
      <p class="benefit__lead">PREPS SKIN FOR</p>
      <p class="benefit__title">MOISTURIZER</p>
      <p class="benefit__copy">exfoliated skin is more receptive to hydration and treatment products.</p>
    </div>
    <p class="net-weight">Net Weight<br>Goes Here</p>
  </section>
  <div class="vertical sample-tag sample-tag--two">SAMPLE 2</div>

</body>
</html>
```